Business Card

Yes I would like you to design me a business card with the logo you just made me

Industry/Entity Type

Business

Colors
33b7a4
00a990
333333
000000
757575
7f7f7f

```html
<!DOCTYPE html>
<html lang="en">
<head>
<meta charset="utf-8">
<title>Marisa Velden Photography – Business Card</title>
<link rel="stylesheet" href="https://fonts.googleapis.com/css2?family=Open+Sans:wght@400;600&family=Tinos:ital,wght@0,400;1,400&display=swap">
<style>
  :root {
    --teal-light: #33b7a4;
    --teal: #00a990;
    --charcoal: #333333;
    --black: #000000;
    --grey: #757575;
    --grey-soft: #7f7f7f;
    --card-black: #1f1f1f;
    --paper: #ffffff;
    --paper-shade: #ececec;
    --backdrop: #e6e6e4;
  }
  * { margin: 0; padding: 0; box-sizing: border-box; }
  html, body {
    width: 1200px; height: 886px; overflow: hidden;
    background: var(--backdrop);
    font-family: "Open Sans", Arial, sans-serif;
  }
  .stage { position: relative; width: 1200px; height: 886px; }
  .card {
    position: absolute; width: 540px; height: 310px; top: 288px;
    overflow: hidden; border-radius: 3px;
    box-shadow: 0 6px 18px rgba(0,0,0,0.18);
  }
  .card--front { left: 40px; background: var(--card-black); }
  .card--back  { left: 620px; background: linear-gradient(160deg, var(--paper) 30%, var(--paper-shade) 100%); }

  .brand { display: flex; align-items: center; gap: 12px; }
  .brand__dot { width: 34px; height: 34px; border-radius: 50%; flex: none; }
  .brand__name { font-weight: 400; white-space: nowrap; letter-spacing: 0.5px; }

  .card--front .brand { position: absolute; left: 0; right: 0; top: 124px; justify-content: center; }
  .card--front .brand__dot { width: 52px; height: 52px; background: var(--teal-light); }
  .card--front .brand__name { font-size: 30px; color: var(--teal-light); }

  .card--back .brand { position: absolute; left: 34px; top: 36px; }
  .card--back .brand__dot { background: var(--charcoal); }
  .card--back .brand__name { font-size: 19px; color: var(--charcoal); }

  .wave { position: absolute; inset: 0; width: 540px; height: 310px; }

  .contact { position: absolute; left: 30px; top: 150px; list-style: none; }
  .contact__item {
    display: flex; align-items: center; gap: 12px;
    color: var(--paper); font-size: 13px; line-height: 24px;
  }
  .contact__icon { width: 14px; height: 14px; flex: none; }

  .person { position: absolute; left: 350px; top: 108px; font-family: "Tinos", "Times New Roman", serif; }
  .person__name { font-style: italic; font-size: 27px; color: var(--teal); }
  .person__role { font-size: 14px; color: var(--charcoal); letter-spacing: 0.5px; margin-top: 2px; }
</style>
</head>
<body>
<main class="stage">
  <section class="card card--front" aria-label="Card front">
    <div class="brand">
      <span class="brand__dot"></span>
      <span class="brand__name">Marisa Velden Photography</span>
    </div>
  </section>

  <section class="card card--back" aria-label="Card back">
    <svg class="wave" viewBox="0 0 540 310" aria-hidden="true">
      <defs>
        <linearGradient id="tealFill" x1="0" y1="0" x2="0" y2="1">
          <stop offset="0" stop-color="#00a990"/>
          <stop offset="1" stop-color="#008f7a"/>
        </linearGradient>
      </defs>
      <path d="M0,142 C120,112 220,124 300,182 C380,240 460,256 540,252 L540,310 L0,310 Z" fill="url(#tealFill)"/>
      <path d="M300,176 C385,232 460,242 540,232 L540,244 C460,252 382,244 300,180 Z" fill="#333333"/>
      <path d="M300,180 C382,244 460,252 540,244 L540,248 C460,256 380,242 300,182 Z" fill="#ffffff"/>
    </svg>

    <div class="brand">
      <span class="brand__dot"></span>
      <span class="brand__name">Marisa Velden Photography</span>
    </div>

    <ul class="contact">
      <li class="contact__item">
        <svg class="contact__icon" viewBox="0 0 14 14" aria-hidden="true"><rect x="3.5" y="0.5" width="7" height="13" rx="1.5" fill="none" stroke="#fff"/><rect x="5" y="2.5" width="4" height="6" fill="#fff"/></svg>
        555-204.7719
      </li>
      <li class="contact__item">
        <svg class="contact__icon" viewBox="0 0 14 14" aria-hidden="true"><rect x="0.5" y="3" width="13" height="9" fill="none" stroke="#fff"/><path d="M0.5,3 L7,8 L13.5,3" fill="none" stroke="#fff"/></svg>
        marisaveldenphoto@inboxmail.com
      </li>
      <li class="contact__item">
        <svg class="contact__icon" viewBox="0 0 14 14" aria-hidden="true"><rect x="1" y="1" width="12" height="12" rx="2" fill="#fff"/></svg>
        /marisaveldenphotography
      </li>
    </ul>

    <div class="person">
      <p class="person__name">Marisa Velden</p>
      <p class="person__role">PHOTOGRAPHER</p>
    </div>
  </section>
</main>
</body>
</html>
```